Business Card Design

We need a business card design for a new dental practice in Brisbane. I'd like the basic details and logo on one side and appointment schedule on the other side. It is based in CBD office area and would prefer a professional and modern design.
Target Market(s)
20-60 years old office workers and residents with high education levels
Industry/Entity Type
Dental
Contact Information for Business Card
Harbourlight Dental
Dr Marcus Lindqvist
Principal Dentist
07 3194 6627
admin@harbourlightdentistry.example.au
www.harbourlightdentistry.example.au
S27, Level 3, Ferndale North Tower, 318 Gorrick St, Alderwood Heights, QLD 4118

```html
<!DOCTYPE html>
<html lang="en">
<head>
<meta charset="utf-8">
<title>Harbourlight Dental – Business Card</title>
<link rel="stylesheet" href="https://fonts.googleapis.com/css2?family=Source+Sans+3:wght@400;600;700&display=swap">
<style>
  :root {
    --backdrop-light: #f2f2f3;
    --backdrop-dark: #b7b8ba;
    --card: #ffffff;
    --brand-blue: #4fb1e3;
    --navy: #0e2136;
    --text-dark: #1a1a1a;
    --text-grey: #7a7a7a;
    --divider: #dcdcdc;
  }
  * { box-sizing: border-box; margin: 0; padding: 0; }
  html, body { width: 1200px; height: 1200px; overflow: hidden; }
  body {
    font-family: "Source Sans 3", "Myriad Pro", sans-serif;
    background: radial-gradient(circle at 50% 50%, var(--backdrop-light) 0%, #e3e3e4 45%, var(--backdrop-dark) 100%);
    position: relative;
  }
  .card {
    position: absolute;
    left: 216px;
    width: 764px;
    height: 463px;
    background: var(--card);
  }
  .card--back { top: 130px; }
  .card--front { top: 600px; height: 462px; }
  .band {
    position: absolute;
    left: 0; width: 100%;
    background: var(--brand-blue);
  }
  .card--back .band { bottom: 0; height: 131px; }
  .card--front .band { top: 0; height: 122px; }
  .card-gap {
    position: absolute;
    left: 216px; width: 764px; top: 593px; height: 7px;
    background: linear-gradient(to bottom, #f7f7f7, var(--divider));
  }

  /* Appointment side */
  .appointment { position: absolute; left: 42px; top: 56px; color: var(--text-grey); }
  .appointment__title { font-size: 21px; font-weight: 400; }
  .appointment__row { font-size: 18px; margin-left: 31px; line-height: 27px; }
  .appointment__row:first-of-type { margin-top: 4px; }
  .box {
    display: inline-block;
    width: 14px; height: 14px;
    border: 1.4px solid var(--text-grey);
    vertical-align: -1px;
    margin-right: 3px;
  }

  .brand-name {
    position: absolute;
    font-weight: 400;
    color: var(--navy);
    white-space: nowrap;
    letter-spacing: 0.2px;
  }
  .card--back .brand-name { right: 56px; bottom: 20px; font-size: 30px; }
  .card--front .brand-name { left: 42px; top: 270px; font-size: 30px; }

  /* Front side */
  .person { position: absolute; right: 72px; top: 36px; text-align: right; }
  .person__name { font-size: 27px; font-weight: 700; color: var(--navy); line-height: 32px; }
  .person__role { font-size: 20px; color: #ffffff; line-height: 26px; }

  .contact { position: absolute; right: 30px; text-align: right; color: var(--text-dark); font-size: 20px; }
  .contact__line { display: flex; justify-content: flex-end; align-items: center; line-height: 26.5px; }
  .contact__icon { width: 16px; height: 16px; margin-left: 20px; flex: none; fill: var(--brand-blue); }
  .contact__icon--blank { visibility: hidden; }
  .contact--address { top: 256px; }
  .contact--reach { top: 357px; }
  .contact--web { top: 426px; }
</style>
</head>
<body>

<section class="card card--back" aria-label="Appointment side">
  <div class="appointment">
    <p class="appointment__title">Next Appointment:</p>
    <p class="appointment__row">Mon<span class="box"></span>Tue<span class="box"></span>Wed<span class="box"></span>Thur<span class="box"></span></p>
    <p class="appointment__row">Date:_________at_____AM<span class="box"></span> PM<span class="box"></span></p>
  </div>
  <div class="band">
    <span class="brand-name">Harbourlight Dental</span>
  </div>
</section>

<div class="card-gap"></div>

<section class="card card--front" aria-label="Contact side">
  <div class="band">
    <div class="person">
      <p class="person__name">Dr Marcus Lindqvist</p>
      <p class="person__role">Principal Dentist</p>
    </div>
  </div>

  <span class="brand-name">Harbourlight Dental</span>

  <div class="contact contact--address">
    <p class="contact__line">S27, Level 3, Ferndale North Tower
      <svg class="contact__icon" viewBox="0 0 16 16" aria-hidden="true"><path d="M8 1.5 1 8h2v6h4v-4h2v4h4V8h2z"/></svg></p>
    <p class="contact__line">318 Gorrick St, Alderwood Heights
      <svg class="contact__icon contact__icon--blank" viewBox="0 0 16 16" aria-hidden="true"></svg></p>
    <p class="contact__line">QLD 4118
      <svg class="contact__icon contact__icon--blank" viewBox="0 0 16 16" aria-hidden="true"></svg></p>
  </div>

  <div class="contact contact--reach">
    <p class="contact__line">07 3194 6627
      <svg class="contact__icon" viewBox="0 0 16 16" aria-hidden="true"><path d="M5 1h6a1 1 0 0 1 1 1v12a1 1 0 0 1-1 1H5a1 1 0 0 1-1-1V2a1 1 0 0 1 1-1zm1 2v7h4V3zm2 9a1 1 0 1 0 0 2 1 1 0 0 0 0-2z"/></svg></p>
    <p class="contact__line">admin@harbourlightdentistry.example.au
      <svg class="contact__icon" viewBox="0 0 16 16" aria-hidden="true"><path d="M1 4h14v1L8 9.5 1 5zm0 2.5 7 4.5 7-4.5V12H1z"/></svg></p>
  </div>

  <div class="contact contact--web">
    <p class="contact__line">www.harbourlightdentistry.example.au
      <svg class="contact__icon" viewBox="0 0 16 16" aria-hidden="true"><g fill="none" stroke="#4fb1e3" stroke-width="1.3"><circle cx="8" cy="8" r="6.5"/><ellipse cx="8" cy="8" rx="2.8" ry="6.5"/><path d="M1.5 8h13M2.6 4.6h10.8M2.6 11.4h10.8"/></g></svg></p>
  </div>
</section>

</body>
</html>
```